Website design using a wordpress template I purchased

I have purchased a wordpress template called "Vantrel" from Plumora and would like to design a website using it for a financial services company. The site simply needs to be informational about the company and a blog. Nothing too involved. The company provides paymaster / escrow services for commodity transactions. I am working on the logo currently and will have it ready to provide shortly. I can provide the content for the informational portion of the site as well. I would like some quick tutoring regarding how to administer the blog portion of the site once built.

```html
<!DOCTYPE html>
<html lang="en">
<head>
<meta charset="utf-8">
<title>Company Website</title>
<link href="https://fonts.googleapis.com/css2?family=Roboto:wght@500;700;900&family=Lato:wght@400;700&display=swap" rel="stylesheet">
<style>
  :root {
    --navy: #0d3168;
    --navy-deep: #0a2448;
    --gold: #f2b705;
    --ink: #1d1d1f;
    --text: #4a4a4a;
    --blog-bg: #e7ecf3;
    --cream: #fffcf1;
    --white: #ffffff;
  }
  * { box-sizing: border-box; margin: 0; padding: 0; }
  html, body { width: 1200px; height: 3622px; overflow: hidden; }
  body { position: relative; font-family: 'Lato', sans-serif; color: var(--text); background: var(--white); }
  .abs { position: absolute; }
  .heading { font-family: 'Roboto', sans-serif; font-weight: 700; color: var(--ink); letter-spacing: 0.5px; }
  .gold { color: var(--gold); }
  .btn {
    position: absolute; display: flex; align-items: center; justify-content: center; gap: 10px;
    border-radius: 24px; font-family: 'Lato', sans-serif; font-weight: 700; font-size: 15px;
  }
  .btn .dot { width: 14px; height: 14px; border-radius: 50%; display: inline-flex; align-items: center; justify-content: center; }
  .btn-navy { background: var(--navy); color: var(--white); }
  .btn-navy .dot { background: var(--white); }
  .btn-white { background: var(--white); color: var(--ink); }
  .btn-white .dot { background: var(--ink); }
  .btn-gold { background: var(--gold); color: var(--white); }
  .btn-gold .dot { background: var(--white); }
  .btn-outline { border: 2px solid var(--gold); color: var(--ink); background: transparent; }
  .btn-outline .dot { background: var(--ink); }
  .para { font-size: 13px; line-height: 24.7px; }

  /* Hero */
  .hero { left: 0; top: 0; width: 1200px; height: 691px;
    background: radial-gradient(circle at 80% 30%, #2a4f7f 0%, transparent 40%),
                linear-gradient(110deg, #0c2341 0%, #173a63 45%, #0e2747 100%); }
  .hero-title { left: 112px; top: 270px; font-family: 'Roboto', sans-serif; font-weight: 700; font-size: 48px; line-height: 59px; color: var(--white); }
  .site-header { left: 75px; top: 0; width: 1049px; height: 95px; background: var(--white); border-radius: 0 0 22px 22px; }
  .brand { left: 32px; top: 32px; font-family: 'Roboto', sans-serif; font-weight: 700; font-size: 27px; color: var(--ink); letter-spacing: 0.5px; }
  .nav a { position: absolute; top: 38px; font-size: 15px; font-weight: 700; color: var(--ink); text-decoration: none; }
  .slider-dots { left: 568px; top: 643px; display: flex; gap: 7px; }
  .slider-dots span { width: 7px; height: 7px; border-radius: 50%; background: var(--white); }
  .slider-dots span.on { background: var(--gold); }

  /* Framed photos */
  .frame-gold { border: 2px solid #f5d77c; border-radius: 8px 48px 8px 48px; }
  .photo { border: 6px solid var(--white); border-radius: 8px 48px 8px 48px; box-shadow: 0 4px 16px rgba(0,0,0,0.12); }

  /* Blog */
  .blog { left: 0; top: 1309px; width: 1200px; height: 776px; background: var(--blog-bg); }
  .card { position: absolute; top: 1465px; width: 308px; height: 443px; background: var(--white); box-shadow: 0 2px 6px rgba(0,0,0,0.06); }
  .card .thumb { position: absolute; left: 5px; top: 6px; width: 298px; height: 202px; }
  .card .date { position: absolute; left: 29px; top: 197px; height: 34px; padding: 0 16px; background: var(--navy); color: var(--white); border-radius: 0 0 18px 18px; font-size: 13px; display: flex; align-items: center; gap: 12px; }
  .card h3 { position: absolute; left: 29px; top: 248px; width: 265px; font-family: 'Lato', sans-serif; font-weight: 400; font-size: 17px; line-height: 23px; color: #333; }
  .card p { position: absolute; left: 29px; top: 308px; width: 245px; font-size: 11.5px; line-height: 18.8px; color: #555; }
  .card .more { position: absolute; left: 29px; top: 400px; font-size: 13px; font-weight: 700; color: var(--navy); text-decoration: underline; display: flex; align-items: center; gap: 6px; }
  .card .more .dot { width: 15px; height: 15px; border-radius: 50%; background: var(--navy); display: inline-flex; align-items: center; justify-content: center; }
  .carousel-arrow { width: 22px; height: 22px; border-radius: 50%; background: #a9adb3; display: flex; align-items: center; justify-content: center; }

  /* Footer */
  .footer { left: 0; top: 3337px; width: 1200px; height: 285px; background: linear-gradient(180deg, #0e3770 0%, #0a2c5c 100%); }
  .footer-nav { left: 0; top: 3520px; width: 1200px; display: flex; justify-content: center; gap: 22px; color: var(--white); font-size: 14px; font-weight: 700; }
  .footer-nav span.sep { font-weight: 400; }
  .social { left: 567px; top: 3473px; display: flex; gap: 8px; }
  .social span { width: 19px; height: 19px; border-radius: 50%; background: var(--white); }
  .social span.alt { background: var(--gold); }
</style>
</head>
<body>

<!-- Hero -->
<section class="abs hero" role="img" aria-label="Businessman in a dark suit cupping hands around a glowing dollar sign, bokeh lights"></section>
<header class="abs site-header">
  <div class="abs brand">COMPANY <span class="gold">LOGO</span></div>
  <nav class="nav">
    <a style="left:346px">HOME</a>
    <a style="left:430px">ABOUT US</a>
    <a style="left:541px">SERVICES</a>
    <a style="left:647px">BLOG</a>
    <a style="left:725px">CONTACT US</a>
  </nav>
  <div class="btn btn-navy" style="left:866px;top:25px;width:151px;height:44px;">GET STARTED <span class="dot"><svg width="8" height="8" viewBox="0 0 8 8"><path d="M1 4h5M4 1.5L6.5 4 4 6.5" stroke="#0d3168" stroke-width="1.4" fill="none"/></svg></span></div>
</header>
<h1 class="abs hero-title"><span class="gold">LIVE</span> LIFE <span class="gold">TODAY.</span><br>BE <span class="gold">CONFIDENT</span> ABOUT<br><span class="gold">TOMORROW</span>.</h1>
<div class="btn btn-white" style="left:112px;top:475px;width:149px;height:45px;">GET STARTED <span class="dot"><svg width="8" height="8" viewBox="0 0 8 8"><path d="M1 4h5M4 1.5L6.5 4 4 6.5" stroke="#fff" stroke-width="1.4" fill="none"/></svg></span></div>
<div class="abs slider-dots"><span></span><span></span><span class="on"></span><span></span><span></span></div>

<!-- About -->
<h2 class="abs heading" style="left:112px;top:788px;font-size:38px;">ABOUT <span class="gold">THE COMPANY</span></h2>
<p class="abs para" style="left:112px;top:856px;width:470px;">Contrary to popular belief, Lorem Ipsum is not simply random text. It has roots in a piece of classical Latin literature from 45 BC, making it over 2000 years old. Edwin Halvorsen, a Latin professor at Marrowfield College in Norvale, looked up one of the more obscure Latin words, consectetur, from a Lorem Ipsum passage, and going through the cites of the word in classical literature, discovered the undoubtable source.</p>
<p class="abs para" style="left:112px;top:1029px;width:470px;">Contrary to popular belief, Lorem Ipsum is not simply random text. It has roots in a piece of classical Latin literature from 45 BC, making it over 2000 years old. Edwin Halvorsen, a Latin professor at Marrowfield College in Norvale, looked up one of the more obscure Latin words</p>
<div class="btn btn-navy" style="left:112px;top:1159px;width:149px;height:45px;">READ MORE <span class="dot"><svg width="8" height="8" viewBox="0 0 8 8"><path d="M1 4h5M4 1.5L6.5 4 4 6.5" stroke="#0d3168" stroke-width="1.4" fill="none"/></svg></span></div>
<div class="abs frame-gold" style="left:672px;top:849px;width:438px;height:376px;"></div>
<div class="abs photo" role="img" aria-label="Business meeting with a presenter standing beside colleagues at a table near bright windows" style="left:614px;top:794px;width:476px;height:406px;background:linear-gradient(135deg,#e9ecee 0%,#cfd3d4 45%,#6b5a4a 80%,#3c3128 100%);"></div>

<!-- Blog -->
<section class="abs blog"></section>
<h2 class="abs heading" style="left:0;top:1392px;width:1200px;text-align:center;font-size:38px;">LATEST <span class="gold">BLOG</span></h2>
<div class="abs carousel-arrow" style="left:60px;top:1676px;"><svg width="10" height="10" viewBox="0 0 10 10"><path d="M8 5H2M4.5 2L2 5l2.5 3" stroke="#fff" stroke-width="1.6" fill="none"/></svg></div>
<div class="abs carousel-arrow" style="left:1117px;top:1676px;"><svg width="10" height="10" viewBox="0 0 10 10"><path d="M2 5h6M5.5 2L8 5 5.5 8" stroke="#fff" stroke-width="1.6" fill="none"/></svg></div>

<article class="card" style="left:119px;">
  <div class="thumb" role="img" aria-label="Business team chatting on sofas in a bright office" style="background:linear-gradient(135deg,#dfe5ea 0%,#9fb0c0 50%,#3a4a5e 100%);"></div>
  <div class="date"><svg width="14" height="14" viewBox="0 0 14 14"><rect x="1" y="2.5" width="12" height="10.5" rx="1" stroke="#fff" fill="none"/><path d="M1 5.5h12M4 1v3M10 1v3" stroke="#fff"/></svg>October 20, 2022</div>
  <h3>Contrary to popular belief, Lorem Ipsum is&nbsp; random text.</h3>
  <p>The standard chunk of Lorem Ipsum used since the 1500s is reproduced below for those interested. Sections 1.10.32 and 1.10.33 from "de Veritate Rerum et Formis</p>
  <div class="more">Read More <span class="dot"><svg width="8" height="8" viewBox="0 0 8 8"><path d="M1 4h5M4 1.5L6.5 4 4 6.5" stroke="#fff" stroke-width="1.4" fill="none"/></svg></span></div>
</article>
<article class="card" style="left:445px;">
  <div class="thumb" role="img" aria-label="Hands reviewing charts on a tablet beside a laptop and coffee cup" style="background:linear-gradient(135deg,#f2f3f4 0%,#c8ced4 55%,#6e7a86 100%);"></div>
  <div class="date"><svg width="14" height="14" viewBox="0 0 14 14"><rect x="1" y="2.5" width="12" height="10.5" rx="1" stroke="#fff" fill="none"/><path d="M1 5.5h12M4 1v3M10 1v3" stroke="#fff"/></svg>October 20, 2022</div>
  <h3>Contrary to popular belief, Lorem Ipsum is&nbsp; random text.</h3>
  <p>The standard chunk of Lorem Ipsum used since the 1500s is reproduced below for those interested. Sections 1.10.32 and 1.10.33 from "de Veritate Rerum et Formis</p>
  <div class="more">Read More <span class="dot"><svg width="8" height="8" viewBox="0 0 8 8"><path d="M1 4h5M4 1.5L6.5 4 4 6.5" stroke="#fff" stroke-width="1.4" fill="none"/></svg></span></div>
</article>
<article class="card" style="left:774px;">
  <div class="thumb" role="img" aria-label="Three colleagues discussing work around a laptop" style="background:linear-gradient(135deg,#e4e6e4 0%,#a9b0ab 50%,#3f4a48 100%);"></div>
  <div class="date"><svg width="14" height="14" viewBox="0 0 14 14"><rect x="1" y="2.5" width="12" height="10.5" rx="1" stroke="#fff" fill="none"/><path d="M1 5.5h12M4 1v3M10 1v3" stroke="#fff"/></svg>October 20, 2022</div>
  <h3>Contrary to popular belief, Lorem Ipsum is&nbsp; random text.</h3>
  <p>The standard chunk of Lorem Ipsum used since the 1500s is reproduced below for those interested. Sections 1.10.32 and 1.10.33 from "de Veritate Rerum et Formis</p>
  <div class="more">Read More <span class="dot"><svg width="8" height="8" viewBox="0 0 8 8"><path d="M1 4h5M4 1.5L6.5 4 4 6.5" stroke="#fff" stroke-width="1.4" fill="none"/></svg></span></div>
</article>
<div class="btn btn-gold" style="left:440px;top:1947px;width:147px;height:44px;">VIEW MORE <span class="dot"><svg width="8" height="8" viewBox="0 0 8 8"><path d="M1 4h5M4 1.5L6.5 4 4 6.5" stroke="#f2b705" stroke-width="1.4" fill="none"/></svg></span></div>
<div class="btn btn-outline" style="left:611px;top:1947px;width:149px;height:44px;">GET STARTED <span class="dot"><svg width="8" height="8" viewBox="0 0 8 8"><path d="M1 4h5M4 1.5L6.5 4 4 6.5" stroke="#fff" stroke-width="1.4" fill="none"/></svg></span></div>

<!-- Vision -->
<section class="abs" style="left:0;top:2085px;width:1200px;height:629px;background:var(--cream);"></section>
<div class="abs" role="img" aria-label="Family running with arms outstretched through a golden meadow at sunset" style="left:0;top:2340px;width:1200px;height:374px;background:linear-gradient(180deg,var(--cream) 0%,#f3e2bf 30%,#c9a36b 65%,#7a5a34 100%);"></div>
<h2 class="abs heading" style="left:0;top:2165px;width:1200px;text-align:center;font-size:38px;">HAVE A <span class="gold">VISION</span>. MAKE A <span class="gold">PLAN</span>. BE <span class="gold">WELL</span>.</h2>
<p class="abs" style="left:280px;top:2223px;width:640px;text-align:center;font-size:13px;line-height:24px;">Lorem ipsum dolor sit amet, consectetur adipiscing elit, sed do eiusmod tempor incididunt ut labore et dolore magna aliqua. Quis ipsum suspendisse ultrices gravida.</p>
<div class="btn btn-navy" style="left:525px;top:2304px;width:149px;height:44px;">GET STARTED <span class="dot"><svg width="8" height="8" viewBox="0 0 8 8"><path d="M1 4h5M4 1.5L6.5 4 4 6.5" stroke="#0d3168" stroke-width="1.4" fill="none"/></svg></span></div>

<!-- Financial services -->
<div class="abs frame-gold" style="left:91px;top:2877px;width:440px;height:373px;"></div>
<div class="abs photo" role="img" aria-label="Smiling business team stacking hands together over a desk with a laptop" style="left:112px;top:2826px;width:470px;height:404px;background:linear-gradient(135deg,#d9dde0 0%,#9ea7ae 40%,#4b5560 75%,#f0f0ee 100%);"></div>
<h2 class="abs heading" style="left:617px;top:2816px;font-size:38px;line-height:45px;">THE POWER OF<br><span class="gold">FINANCIAL SERVICES</span></h2>
<p class="abs para" style="left:617px;top:2926px;width:470px;">Contrary to popular belief, Lorem Ipsum is not simply random text. It has roots in a piece of classical Latin literature from 45 BC, making it over 2000 years old. Edwin Halvorsen, a Latin professor at Marrowfield College in Norvale, looked up one of the more obscure Latin words</p>
<p class="abs para" style="left:617px;top:3050px;width:470px;">Contrary to popular belief, Lorem Ipsum is not simply random text. It has roots in a piece of classical Latin literature from 45 BC, making it over 2000 years old. Edwin Halvorsen, a Latin professor at Marrowfield College in Norvale, looked up one of the more obscure Latin words</p>
<div class="btn btn-navy" style="left:617px;top:3188px;width:149px;height:44px;">READ MORE <span class="dot"><svg width="8" height="8" viewBox="0 0 8 8"><path d="M1 4h5M4 1.5L6.5 4 4 6.5" stroke="#0d3168" stroke-width="1.4" fill="none"/></svg></span></div>

<!-- Footer -->
<footer class="abs footer"></footer>
<div class="abs" style="left:0;top:3390px;width:1200px;text-align:center;font-family:'Roboto',sans-serif;font-weight:700;font-size:48px;color:var(--white);letter-spacing:1px;">COMPANY <span class="gold">LOGO</span></div>
<div class="abs social"><span></span><span class="alt"></span><span></span></div>
<nav class="abs footer-nav">
  <span>HOME</span><span class="sep">|</span><span>ABOUT US</span><span class="sep">|</span><span>SERVICES</span><span class="sep">|</span><span>LATEST BLOGS</span><span class="sep">|</span><span>CONTACT US</span><span class="sep">|</span><span>SITE MAP</span>
</nav>
<div class="abs" style="left:0;top:3567px;width:1200px;text-align:center;font-size:11px;color:var(--white);">© 2022 Copyright company Name | All rights Reserved.</div>

</body>
</html>
```